Redesign Australian netball site

Existing website needs a new look and feel - http://kelvalecourts.com.au/
We require a homepage design that contains 3 sections: Chatterly feed, Recent Articles and Sponsors.
We also require a subpage design showing a main content area and a right hand sidebar (containing panels for login, chatterly feed, articles and sponsors)
Updates

Hopefully the updated brief provides more information now but if there are further questions then feel free to email me at ts@brightwharf.com.au

Reason: To allow additional submissions and design tweaks

Target Market(s)

The site needs to target parents of younger players, older players themselves and sponsors.

Requirements
Must have
• Header must contain:
1. current logo from http://kelvalecourts.com.au/
2. The slogan "Fun, Fitness, Fair Competition - Play Netball"
3. A space for a Platinum Sponsor (see current site)

Top level navigation should be:
1. Seniors
2. Juniors
3. Zippets
4. Sponsors
5. Special Offers
6. About Us
7. Umpires

```html
<!DOCTYPE html>
<html lang="en">
<head>
<meta charset="utf-8">
<title>Kelvale Netball</title>
<link rel="stylesheet" href="https://fonts.googleapis.com/css2?family=Questrial&family=Arimo:wght@400;700&display=swap">
<style>
:root{
  --navy:#0b2a5c;
  --pink:#e0307e;
  --magenta:#c8238a;
  --grey-text:#6a6a6a;
  --rule:#cfcfcf;
  --page:#f6f6f7;
  --white:#ffffff;
  --heading:"Questrial",sans-serif;
  --body:"Arimo",sans-serif;
}
*{box-sizing:border-box;margin:0;padding:0}
html,body{width:850px;height:1200px;overflow:hidden;background:var(--page)}
.canvas{position:relative;width:850px;height:1200px;overflow:hidden;background:var(--page);font-family:var(--body);color:var(--grey-text)}
.abs{position:absolute}
.top-stripe{left:0;top:0;width:850px;height:4px;background:var(--pink)}
.brand{left:83px;top:10px;width:180px;text-align:center}
.brand-dot{display:block;width:50px;height:50px;border-radius:50%;background:var(--navy);margin:8px auto 14px}
.brand-name{font-family:var(--heading);font-size:14px;color:var(--navy);line-height:16px}
.brand-slogan{font-family:var(--heading);font-size:7.5px;color:var(--pink);margin-top:2px;letter-spacing:.2px}
.utility{right:92px;top:35px;font-family:var(--heading);font-size:8px;color:var(--navy)}
.utility span{margin:0 4px}
.search{left:594px;top:71px;width:169px;height:23px;background:var(--white);border:2px solid #e2e2e2}
.search svg{position:absolute;right:6px;top:5px}
.main-nav{left:0;top:124px;width:850px;height:28px;background:var(--navy)}
.main-nav a{position:absolute;top:8px;font-family:var(--heading);font-size:10.5px;color:var(--white);text-decoration:none;letter-spacing:.2px}
.hero{left:0;top:152px;width:850px;height:279px;background:linear-gradient(180deg,#3a3650 0%,#6a4f58 45%,#4a4e5e 100%)}
.hero-dots{left:406px;top:411px;display:flex;gap:6px}
.hero-dots i{width:7px;height:7px;border-radius:50%;background:#2a2a2a}
.hero-dots i:first-child{background:var(--pink)}
.divider-v{left:541px;top:431px;width:1px;height:701px;background:#e4e4e4}
.section-title{font-family:var(--heading);font-size:13.5px;color:var(--navy);letter-spacing:.2px}
.section-rule{height:2px;background:var(--rule)}
.article{left:84px;width:446px;height:159px}
.article-title{position:absolute;left:1px;top:0;font-family:var(--heading);font-size:11px;color:var(--navy)}
.article-thumb{position:absolute;left:1px;top:22px;width:70px;height:70px;background:linear-gradient(160deg,#8a6f63,#3a4b6e)}
.article-text{position:absolute;left:78px;top:20px;width:368px;font-size:7.6px;line-height:12.8px;color:var(--grey-text)}
.article-text p+p{margin-top:12.8px}
.article-dots{position:absolute;left:0;top:110px;width:236px;border-top:1px dotted #bdbdbd}
.article-meta{position:absolute;left:1px;top:117px;width:445px;font-size:7.6px;color:var(--grey-text)}
.article-meta b{font-weight:400;color:var(--pink)}
.comments{position:absolute;right:0;top:0}
.comments svg{vertical-align:-1px;margin-right:6px}
.article-rule{position:absolute;left:0;top:133px;width:446px;height:1px;background:#dedede}
.platinum{left:552px;top:446px;width:213px;height:60px;background:var(--navy)}
.platinum-label{position:absolute;left:14px;top:13px;font-family:var(--heading);font-size:14px;line-height:17px;color:var(--white);letter-spacing:.6px}
.sponsor-slot{position:absolute;left:116px;top:10px;width:86px;height:38px;background:#e02a2f;border:1px solid #f3f3f3}
.sponsor-slot span{position:absolute;left:0;top:13px;width:100%;text-align:center;font-family:var(--body);font-size:8px;color:var(--white)}
.pager{left:737px;top:532px;display:flex;gap:3px}
.pager i{width:12px;height:12px;border:1px solid #d5d5d5;background:var(--white);display:flex;align-items:center;justify-content:center}
.event{left:552px;width:213px}
.event-icon{position:absolute;left:0;top:0}
.event-title{position:absolute;left:30px;top:0;font-size:8.6px;color:var(--magenta);white-space:nowrap}
.event-date{position:absolute;left:30px;top:14px;font-size:7px;color:var(--grey-text)}
.event-desc{position:absolute;left:30px;top:26px;width:183px;font-size:7.4px;line-height:12.8px;text-align:justify;color:var(--grey-text)}
.event-rule{position:absolute;left:30px;top:54px;width:183px;height:1px;background:#dedede}
.like-btn{left:723px;top:772px;width:34px;height:14px;border:1px solid #c5c9d6;background:#f3f4f8;font-size:7px;color:#3b5b9b;padding:2px 0 0 5px}
.feed-item{left:552px;width:213px;height:40px}
.feed-avatar{position:absolute;left:0;top:0;width:30px;height:30px;background:linear-gradient(160deg,#c9a58f,#6d5347)}
.feed-text{position:absolute;left:42px;top:2px;width:171px;font-size:7.6px;line-height:10.5px;color:var(--grey-text)}
.feed-text b{font-weight:400;color:#b34a16}
.feed-text small{font-size:6.8px}
.feed-rule{position:absolute;left:0;top:38px;width:213px;height:1px;background:#dedede}
.account{left:552px;top:958px;width:213px;height:151px;background:var(--navy)}
.account h3{position:absolute;left:7px;top:5px;font-family:var(--heading);font-weight:400;font-size:13px;color:var(--white);letter-spacing:.5px}
.account-field{position:absolute;left:6px;width:199px;height:23px;background:var(--white);border-radius:2px}
.remember{position:absolute;left:13px;top:100px;font-size:7.8px;color:var(--white);display:flex;align-items:center;gap:11px}
.remember i{width:8px;height:8px;background:var(--white)}
.login-btn{position:absolute;left:147px;top:92px;width:58px;height:24px;background:var(--pink);font-family:var(--heading);font-size:12.5px;color:var(--white);text-align:center;line-height:24px}
.account-links{position:absolute;left:41px;top:131px;font-size:7.8px;color:var(--white)}
.account-links span{margin:0 11px}
.footer{left:0;top:1132px;width:850px;height:68px;background:var(--navy)}
.footer-text{position:absolute;left:86px;top:22px;font-size:7.8px;line-height:20.5px;color:var(--white)}
.social{position:absolute;left:643px;top:16px;display:flex;gap:3px}
.social i{width:22px;height:22px;border-radius:50%;background:var(--white)}
</style>
</head>
<body>
<div class="canvas">
  <div class="abs top-stripe"></div>

  <header>
    <div class="abs brand">
      <span class="brand-dot"></span>
      <div class="brand-name">Kelvale Netball</div>
      <div class="brand-slogan">Fun, Fitness, Fair Competition - Play Netball</div>
    </div>
    <div class="abs utility">HOME<span>|</span>HELP<span>|</span>SITEMAP</div>
    <div class="abs search">
      <svg width="10" height="10" viewBox="0 0 10 10"><circle cx="6" cy="4" r="3" fill="none" stroke="#c4c4c4" stroke-width="1.3"/><line x1="4" y1="6" x2="1" y2="9" stroke="#c4c4c4" stroke-width="1.6"/></svg>
    </div>
  </header>

  <nav class="abs main-nav">
    <a style="left:110px">SENIORS</a>
    <a style="left:199px">JUNIORS</a>
    <a style="left:290px">ZIPPETS</a>
    <a style="left:373px">SPONSORS</a>
    <a style="left:474px">SPECIAL OFFERS</a>
    <a style="left:602px">ABOUT US</a>
    <a style="left:699px">UMPIRES</a>
  </nav>

  <div class="abs hero" role="img" aria-label="Action photo of netball players leaping for the ball in a packed arena"></div>
  <div class="abs hero-dots"><i></i><i></i><i></i></div>

  <div class="abs divider-v"></div>

  <main>
    <h2 class="abs section-title" style="left:84px;top:446px;font-weight:400">RECENT ARTICLES</h2>
    <div class="abs section-rule" style="left:84px;top:466px;width:446px"></div>

    <article class="abs article" style="top:480px">
      <h3 class="article-title" style="font-weight:400">Shooting from the Hip: Tessa Marlow C Coastline Comets</h3>
      <div class="article-thumb" role="img" aria-label="Player holding a netball overhead"></div>
      <div class="article-text">
        <p>Tessa Marlow – C – Coastline Comets takes 5 with Kelvale Netball</p>
        <p>profile-tessa-marlow1. How old were you when you started playing netball and what club did you play for?<br>I was 10 years old and played for the Elmvale Wrens.<br>2. What do you love about playing netball?</p>
      </div>
      <div class="article-dots"></div>
      <div class="article-meta"><b>Tags:</b> Harbour Herons, National Opals, Netball
        <span class="comments"><svg width="12" height="8" viewBox="0 0 12 8"><ellipse cx="6" cy="3.5" rx="6" ry="3.5" fill="#5a5a5a"/><path d="M3 6 L2 8 L6 6.5Z" fill="#5a5a5a"/></svg>Comments (2)</span></div>
      <div class="article-rule"></div>
    </article>

    <article class="abs article" style="top:639px">
      <h3 class="article-title" style="font-weight:400">Shooting from the Hip: Jorja Pratt</h3>
      <div class="article-thumb" role="img" aria-label="Player passing a netball during a match"></div>
      <div class="article-text">
        <p>Tessa Marlow – C – Coastline Comets takes 5 with Kelvale Netball</p>
        <p>profile-tessa-marlow1. How old were you when you started playing netball and what club did you play for?<br>I was 10 years old and played for the Elmvale Wrens.<br>2. What do you love about playing netball?</p>
      </div>
      <div class="article-meta" style="top:117px"><b>Tags:</b> Harbour Herons, National Opals, Netball
        <span class="comments"><svg width="12" height="8" viewBox="0 0 12 8"><ellipse cx="6" cy="3.5" rx="6" ry="3.5" fill="#5a5a5a"/><path d="M3 6 L2 8 L6 6.5Z" fill="#5a5a5a"/></svg>Comments (2)</span></div>
      <div class="article-rule" style="top:105px"></div>
      <div class="article-rule"></div>
    </article>

    <article class="abs article" style="top:801px">
      <h3 class="article-title" style="font-weight:400">Shoulder Pass – the basis of ALL passing</h3>
      <div class="article-thumb" style="background:linear-gradient(160deg,#6f7a3a,#d8c23a)" role="img" aria-label="Player in yellow making a shoulder pass"></div>
      <div class="article-text">
        <p>Tessa Marlow – C – Coastline Comets takes 5 with Kelvale Netball</p>
        <p>profile-tessa-marlow1. How old were you when you started playing netball and what club did you play for?<br>I was 10 years old and played for the Elmvale Wrens.<br>2. What do you love about playing netball?</p>
      </div>
      <div class="article-meta" style="top:123px"><b>Tags:</b> Harbour Herons, National Opals, Netball
        <span class="comments"><svg width="12" height="8" viewBox="0 0 12 8"><ellipse cx="6" cy="3.5" rx="6" ry="3.5" fill="#5a5a5a"/><path d="M3 6 L2 8 L6 6.5Z" fill="#5a5a5a"/></svg>Comments (2)</span></div>
      <div class="article-rule" style="top:115px"></div>
      <div class="article-rule" style="top:140px"></div>
    </article>

    <article class="abs article" style="top:965px">
      <h3 class="article-title" style="font-weight:400">Kelvale 61 off to a Flying Start!</h3>
      <div class="article-thumb" style="background:linear-gradient(160deg,#5b6d7a,#3447a0)" role="img" aria-label="Team photo of a young junior netball squad"></div>
      <div class="article-text">
        <p>Saturday, 6 April</p>
        <p>saw our youngest team, Kelvale 61, play their first ever game of netball. After only three training sessions, no one was quite sure what to expect! To their coaches' amazement, the girls played a great game, scoring 9 goals!</p>
      </div>
      <div class="article-meta" style="top:122px"><b>Tags:</b> Harbour Herons, National Opals, Netball
        <span class="comments"><svg width="12" height="8" viewBox="0 0 12 8"><ellipse cx="6" cy="3.5" rx="6" ry="3.5" fill="#5a5a5a"/><path d="M3 6 L2 8 L6 6.5Z" fill="#5a5a5a"/></svg>Comments (2)</span></div>
      <div class="article-rule" style="top:114px"></div>
      <div class="article-rule" style="top:141px"></div>
    </article>
  </main>

  <aside>
    <div class="abs platinum">
      <div class="platinum-label">PLATINUM<br>SPONSOR</div>
      <div class="sponsor-slot"><span>Brickwood &amp; Kerr</span></div>
    </div>

    <h2 class="abs section-title" style="left:552px;top:530px;font-weight:400">UPCOMING EVENTS</h2>
    <div class="abs pager">
      <i><svg width="4" height="6" viewBox="0 0 4 6"><path d="M3 0.5 L1 3 L3 5.5" fill="none" stroke="#999"/></svg></i>
      <i><svg width="4" height="6" viewBox="0 0 4 6"><path d="M1 0.5 L3 3 L1 5.5" fill="none" stroke="#999"/></svg></i>
    </div>
    <div class="abs section-rule" style="left:552px;top:551px;width:213px"></div>

    <div class="abs event" style="top:563px">
      <svg class="event-icon" width="22" height="20" viewBox="0 0 22 20"><path d="M2 7 H7 L18 1 V17 L7 12 H2Z" fill="var(--magenta)"/><rect x="4" y="12" width="4" height="7" fill="var(--magenta)"/><rect x="19" y="7" width="3" height="4" fill="var(--magenta)"/></svg>
      <div class="event-title">Senior Fitness followed by Netball Skills</div>
      <div class="event-date">April 15, 2013 | 9:51 am</div>
      <div class="event-desc">Keep up your &nbsp;fitness and ball skills over tje school holidays.</div>
      <div class="event-rule"></div>
    </div>
    <div class="abs event" style="top:632px">
      <svg class="event-icon" width="22" height="20" viewBox="0 0 22 20"><path d="M2 7 H7 L18 1 V17 L7 12 H2Z" fill="var(--magenta)"/><rect x="4" y="12" width="4" height="7" fill="var(--magenta)"/><rect x="19" y="7" width="3" height="4" fill="var(--magenta)"/></svg>
      <div class="event-title">Junior Uniforms – DELIVERY DELAYED</div>
      <div class="event-date">April 15, 2013 | 9:51 am</div>
      <div class="event-desc">Keep up your &nbsp;fitness and ball skills over tje school holidays.</div>
      <div class="event-rule"></div>
    </div>
    <div class="abs event" style="top:699px">
      <svg class="event-icon" width="22" height="20" viewBox="0 0 22 20"><path d="M2 7 H7 L18 1 V17 L7 12 H2Z" fill="var(--magenta)"/><rect x="4" y="12" width="4" height="7" fill="var(--magenta)"/><rect x="19" y="7" width="3" height="4" fill="var(--magenta)"/></svg>
      <div class="event-title">Junior Training ON at this stage.</div>
      <div class="event-date">April 15, 2013 | 9:51 am</div>
      <div class="event-desc">Keep up your &nbsp;fitness and ball skills over tje school holidays.</div>
      <div class="event-rule" style="left:30px"></div>
    </div>

    <h2 class="abs section-title" style="left:552px;top:768px;font-weight:400">CHATTERLY FEED</h2>
    <div class="abs like-btn">Like</div>
    <div class="abs section-rule" style="left:552px;top:789px;width:213px"></div>

    <div class="abs feed-item" style="top:805px">
      <div class="feed-avatar" role="img" aria-label="Profile picture of a feed commenter"></div>
      <div class="feed-text"><b>dana fuller</b> Some stress is natural, but often times stress becomes a problem<br><small>2 mins ago - Reply - Like</small></div>
      <div class="feed-rule"></div>
    </div>
    <div class="abs feed-item" style="top:852px">
      <div class="feed-avatar" role="img" aria-label="Profile picture of a feed commenter"></div>
      <div class="feed-text" style="left:41px"><b>dana fuller</b> Some stress is natural, but often times stress becomes a problem<br><small>2 mins ago - Reply - Like</small></div>
      <div class="feed-rule" style="top:39px"></div>
    </div>
    <div class="abs feed-item" style="top:902px">
      <div class="feed-avatar" role="img" aria-label="Profile picture of a feed commenter"></div>
      <div class="feed-text" style="left:41px"><b>dana fuller</b> Some stress is natural, but often times stress becomes a problem<br><small>2 mins ago - Reply - Like</small></div>
      <div class="feed-rule"></div>
    </div>

    <div class="abs account">
      <h3>MY ACCOUNT</h3>
      <div class="account-field" style="top:29px"></div>
      <div class="account-field" style="top:61px"></div>
      <div class="remember"><i></i>Remember me</div>
      <div class="login-btn">LOGIN</div>
      <div class="account-links">Register<span>|</span>Lost your password?</div>
    </div>
  </aside>

  <footer class="abs footer">
    <div class="footer-text">© 2013 Kelvale Netball Club Inc. | Help<br>Please read our Privacy Policy &amp; Disclaimer. | Committee - Review</div>
    <div class="social"><i></i><i></i><i></i><i></i><i></i></div>
  </footer>
</div>
</body>
</html>
```